City department needs a bold and eye-catching poster design.

We need a poster to promote a survey targeting youth and young adults from 14-29 yr olds in the city of Strathcona County. We want poster designs that are bold, provocative and colourful. We want to poster to be a bright piece of art on the wall. See images attached. REQUIRED COPY: "Need something? We're listening" OR "Have Ideas? We're listening" OR "Your Wish? We're listening"

Target Market(s)

Youth, 14-29 yr olds

Industry/Entity Type

Government

Font styles to use
Sans Serif

Requirements
Must have
• REQUIRED COPY: Need something? We're listening"

```html
<!DOCTYPE html>
<html lang="en">
<head>
<meta charset="utf-8">
<title>Need Something? We're Listening — Youth Survey Poster</title>
<link rel="stylesheet" href="https://fonts.googleapis.com/css2?family=Bebas+Neue&display=swap">
<style>
  :root {
    --page-bg: #e9e7e3;
    --poster-bg: #050505;
    --poster-frame: #ffffff;
    --type-cream: #f7efdf;
    --type-edge: #1a1a1a;
    --mosaic-blue: #5aa8dc;
    --mosaic-green: #6cb04a;
    --mosaic-yellow: #f6d234;
    --mosaic-orange: #f08a24;
    --mosaic-red: #d8283c;
    --mosaic-magenta: #d63a8c;
  }
  * { margin: 0; padding: 0; box-sizing: border-box; }
  html, body {
    width: 1200px;
    height: 697px;
    overflow: hidden;
    background: var(--page-bg);
  }
  .canvas {
    position: relative;
    width: 1200px;
    height: 697px;
  }
  .poster {
    position: absolute;
    left: 382px;
    top: 18px;
    width: 436px;
    height: 660px;
    background: var(--poster-bg);
    outline: 6px solid var(--poster-frame);
    overflow: hidden;
  }
  .mosaic {
    position: absolute;
    inset: 0;
    width: 100%;
    height: 100%;
  }
  .headline {
    position: absolute;
    font-family: "Bebas Neue", "Oswald", sans-serif;
    color: var(--type-cream);
    line-height: 0.78;
    white-space: nowrap;
    text-shadow: 2px 2px 0 var(--type-edge), -1px -1px 0 var(--type-edge);
    transform-origin: 0 0;
  }
  .headline--need {
    left: 28px;
    top: 386px;
    font-size: 167px;
    transform: scaleX(0.8);
  }
  .headline--something {
    left: 250px;
    top: 510px;
    font-size: 134px;
    transform: rotate(-90deg) scaleX(0.84);
  }
  .headline--were {
    left: 31px;
    top: 520px;
    font-size: 61px;
    transform: scaleX(0.8);
  }
  .headline--listening {
    left: 131px;
    top: 519px;
    font-size: 106px;
    transform: scaleX(0.76);
  }
</style>
</head>
<body>
<main class="canvas">
  <article class="poster">
    <svg class="mosaic" viewBox="0 0 558 844" preserveAspectRatio="none" aria-hidden="false">
      <defs>
        <linearGradient id="mosaic-top-tones" x1="0" y1="0" x2="1" y2="1">
          <stop offset="0" stop-color="var(--mosaic-blue)"/>
          <stop offset="0.3" stop-color="var(--mosaic-yellow)"/>
          <stop offset="0.55" stop-color="var(--mosaic-red)"/>
          <stop offset="0.8" stop-color="var(--mosaic-orange)"/>
          <stop offset="1" stop-color="var(--mosaic-magenta)"/>
        </linearGradient>
        <linearGradient id="mosaic-bottom-tones" x1="0" y1="0" x2="1" y2="0">
          <stop offset="0" stop-color="var(--mosaic-magenta)"/>
          <stop offset="0.25" stop-color="var(--mosaic-green)"/>
          <stop offset="0.5" stop-color="var(--mosaic-red)"/>
          <stop offset="0.75" stop-color="var(--mosaic-yellow)"/>
          <stop offset="1" stop-color="var(--mosaic-blue)"/>
        </linearGradient>
      </defs>
      <polygon role="img" aria-label="Colourful triangle mosaic cascading from the top edge"
        fill="url(#mosaic-top-tones)"
        points="0,0 558,0 558,250 500,230 420,160 330,120 290,220 200,230 170,100 90,80 0,140"/>
      <polygon role="img" aria-label="Colourful triangle mosaic along the bottom edge"
        fill="url(#mosaic-bottom-tones)"
        points="0,590 80,560 170,600 260,650 400,700 558,740 558,844 0,844"/>
    </svg>
    <h1 class="headline-group">
      <span class="headline headline--need">Need</span>
      <span class="headline headline--something">Something?</span>
      <span class="headline headline--were">We're</span>
      <span class="headline headline--listening">Listening</span>
    </h1>
  </article>
</main>
</body>
</html>
```